Posters to advertise a jewellery design school

I would like two pieces of artwork designing for our jewellery design school in Kuala Lumpur Malaysia.
60cm by 180cm poster
100cm by 100cm poster

My personal style is ‘perfectly imperfect’ but we wold like to show that we give quality classes in a fun and artistic / creative environment

The posters must contain our logo and you can choose to use as many or as few images as you like to tell the story or even include hand drawn line images.

https://files.brambleshare.net/folders/7kQzWmR2pLxT8nYv__HbS3dFj6cNa9Ec?usp=sharing

Please include the following wording on the poster
So you want to be a jewellery designer?

Part time and full-time classes available in:
Silversmithing
Jewellery design and rendering
Stone setting
Gemmology
Enamelling
Computer aided design
60cm by 180cm poster
100cm by 100cm poster

The posters must contain our logo and you can choose to use as many or as few images as you like to tell the story.

Silversmithing
Stone setting
Gemmology
Enamelling
Computer aided design

60cm by 180cm poster
100cm by 100cm poster

Silversmithing
Stone setting
Gemmology
Enamelling
Computer aided design

```html
<!DOCTYPE html>
<html lang="en">
<head>
<meta charset="utf-8">
<title>Mira Hollis jewellery – school posters</title>
<link href="https://fonts.googleapis.com/css2?family=Sorts+Mill+Goudy&family=Tinos:wght@700&family=Montserrat:wght@300&display=swap" rel="stylesheet">
<style>
  :root {
    --teal: #3a9a85;
    --slate: #4f595c;
    --ink: #4a4f52;
    --paper: #ffffff;
    --text-dark: #3f4446;
  }
  html, body { margin: 0; padding: 0; overflow: hidden; background: var(--paper); }
  .canvas { position: relative; width: 1200px; height: 1200px; overflow: hidden; background: var(--paper); }
  .abs { position: absolute; }
  .band { background: var(--teal); }
  .band-top { border-radius: 0 0 50% 50% / 0 0 18px 18px; }
  .photo { position: absolute; }
  .brand-mark { position: absolute; border: 2px solid var(--ink); border-radius: 50%; box-sizing: border-box; }
  .brand-name {
    position: absolute; text-align: center; color: var(--ink);
    font-family: "Montserrat", sans-serif; font-weight: 300; line-height: 1; white-space: nowrap;
  }
  .headline {
    position: absolute; text-align: center; color: var(--teal);
    font-family: "Sorts Mill Goudy", serif; line-height: 1.2; margin: 0; font-weight: 400;
    -webkit-text-stroke: 0.35px var(--teal); white-space: nowrap;
  }
  .headline.wrap { white-space: normal; }
  .course-list {
    position: absolute; list-style: none; margin: 0; padding: 0; text-align: center;
    font-family: "Tinos", serif; font-weight: 700; white-space: nowrap;
  }
  .course-panel { background: var(--slate); }
  .course-panel .course-list { color: #fff; }

  /* photo tones */
  .photo-bench {
    background:
      radial-gradient(ellipse 30% 45% at 12% 62%, #2a2624 0%, rgba(42,38,36,0) 100%),
      radial-gradient(ellipse 22% 30% at 36% 42%, #3b2f2a 0%, rgba(59,47,42,0) 100%),
      radial-gradient(ellipse 28% 40% at 33% 70%, #e8e6e3 0%, rgba(232,230,227,0) 100%),
      radial-gradient(ellipse 45% 35% at 72% 85%, #c9955e 0%, rgba(201,149,94,0) 100%),
      radial-gradient(ellipse 20% 40% at 62% 30%, #2b2b2d 0%, rgba(43,43,45,0) 100%),
      linear-gradient(180deg, #e5e1dc 0%, #b7b2ab 45%, #a9825a 100%);
  }
  .photo-pieces {
    background:
      radial-gradient(ellipse 22% 25% at 38% 55%, #d05a30 0%, rgba(208,90,48,0) 100%),
      radial-gradient(ellipse 30% 18% at 22% 18%, #b9b5ad 0%, rgba(185,181,173,0) 100%),
      radial-gradient(ellipse 20% 16% at 82% 20%, #b36a46 0%, rgba(179,106,70,0) 100%),
      radial-gradient(ellipse 18% 14% at 88% 78%, #6fb7c4 0%, rgba(111,183,196,0) 100%),
      radial-gradient(ellipse 30% 20% at 40% 85%, #a9a6a0 0%, rgba(169,166,160,0) 100%),
      linear-gradient(135deg, #2a2b2d, #47484a 55%, #232425);
  }
  .photo-earrings {
    background:
      radial-gradient(ellipse 16% 22% at 38% 28%, #2f6f8c 0%, rgba(47,111,140,0) 100%),
      radial-gradient(ellipse 14% 18% at 30% 52%, #6d5a3c 0%, rgba(109,90,60,0) 100%),
      radial-gradient(ellipse 24% 20% at 62% 78%, #2c3550 0%, rgba(44,53,80,0) 100%),
      radial-gradient(ellipse 28% 24% at 66% 80%, #d7b14a 0%, rgba(215,177,74,0) 100%),
      #ffffff;
  }
  .photo-rings {
    background:
      radial-gradient(circle at 10% 20%, #1d3a3a 0 7%, rgba(29,58,58,0) 14%),
      radial-gradient(circle at 40% 22%, #f1eee4 0 7%, rgba(241,238,228,0) 13%),
      radial-gradient(circle at 50% 62%, #2a5a66 0 9%, rgba(42,90,102,0) 16%),
      radial-gradient(circle at 78% 44%, #1e2324 0 6%, rgba(30,35,36,0) 12%),
      radial-gradient(circle at 24% 58%, #252020 0 5%, rgba(37,32,32,0) 11%),
      radial-gradient(circle at 90% 30%, #3c5a2a 0 5%, rgba(60,90,42,0) 11%),
      linear-gradient(90deg, #d8b94e, #e2dfd6 18%, #d9ba5c 34%, #cfa47e 50%, #d8bb52 66%, #e3e0d8 82%, #d6b650);
  }
  .photo-group {
    background:
      radial-gradient(ellipse 8% 16% at 18% 32%, #dcd6cc 0%, rgba(220,214,204,0) 100%),
      radial-gradient(ellipse 50% 40% at 50% 80%, #22283a 0%, rgba(34,40,58,0) 100%),
      radial-gradient(ellipse 10% 25% at 52% 60%, #f0f0f0 0%, rgba(240,240,240,0) 100%),
      radial-gradient(ellipse 10% 22% at 92% 65%, #ededeb 0%, rgba(237,237,235,0) 100%),
      radial-gradient(ellipse 5% 6% at 5% 8%, #c8302a 0%, rgba(200,48,42,0) 100%),
      linear-gradient(180deg, #5d6064 0%, #6f6c66 45%, #3a3f4a 100%);
  }
  .photo-tools {
    background:
      radial-gradient(ellipse 18% 35% at 25% 50%, #3a2420 0%, rgba(58,36,32,0) 100%),
      radial-gradient(ellipse 28% 14% at 45% 10%, #5a5a5c 0%, rgba(90,90,92,0) 100%),
      radial-gradient(ellipse 22% 30% at 76% 45%, #5e5e60 0%, rgba(94,94,96,0) 100%),
      radial-gradient(ellipse 12% 30% at 52% 70%, #6e6e70 0%, rgba(110,110,112,0) 100%),
      #ffffff;
  }
  .photo-class {
    background:
      radial-gradient(ellipse 30% 40% at 22% 30%, #2a2422 0%, rgba(42,36,34,0) 100%),
      radial-gradient(ellipse 35% 45% at 68% 75%, #e7c3c7 0%, rgba(231,195,199,0) 100%),
      radial-gradient(ellipse 18% 20% at 64% 28%, #d8c08c 0%, rgba(216,192,140,0) 100%),
      radial-gradient(ellipse 40% 20% at 40% 92%, #b89a78 0%, rgba(184,154,120,0) 100%),
      linear-gradient(135deg, #6b5d50 0%, #a69682 50%, #8a7a68 100%);
  }
  .photo-setting {
    background:
      radial-gradient(ellipse 35% 30% at 80% 35%, #2c3346 0%, rgba(44,51,70,0) 100%),
      radial-gradient(ellipse 45% 30% at 35% 62%, #eab7c2 0%, rgba(234,183,194,0) 100%),
      radial-gradient(ellipse 22% 14% at 30% 36%, #e3cfa4 0%, rgba(227,207,164,0) 100%),
      radial-gradient(ellipse 30% 12% at 80% 8%, #6b4a40 0%, rgba(107,74,64,0) 100%),
      linear-gradient(180deg, #efebe6 0%, #e4dbd4 55%, #c9ac90 100%);
  }
</style>
</head>
<body>
<div class="canvas">

  <section class="poster-tall">
    <div class="abs band band-top" style="left:99px; top:0; width:400px; height:72px;" role="img" aria-label="Teal woven lattice pattern band"></div>

    <div class="brand-mark" style="left:253px; top:78px; width:96px; height:96px;"></div>
    <div class="brand-name" style="left:99px; top:190px; width:400px; font-size:31px; letter-spacing:1px;">MIRA HOLLIS</div>
    <div class="brand-name" style="left:99px; top:226px; width:400px; font-size:17px; letter-spacing:3px;">jewellery</div>

    <h1 class="headline" style="left:99px; top:255px; width:400px; font-size:22.5px;">So you want to be a jewellery designer?</h1>

    <div class="photo photo-bench" style="left:99px; top:287px; width:400px; height:247px;" role="img" aria-label="Student at a jeweller's bench working under a microscope"></div>
    <div class="photo photo-pieces" style="left:99px; top:550px; width:220px; height:147px;" role="img" aria-label="Handmade silver cuff, pendants and enamelled pieces on a dark surface"></div>
    <div class="photo photo-earrings" style="left:328px; top:534px; width:152px; height:163px;" role="img" aria-label="Gemstone drop earrings and a gold cocktail ring"></div>

    <h2 class="headline" style="left:99px; top:710px; width:400px; font-size:21.5px;">Part time and full-time classes available in:</h2>
    <div class="abs course-panel" style="left:99px; top:738px; width:400px; height:130px;">
      <ul class="course-list" style="left:0; top:-1px; width:400px; font-size:17.8px; line-height:21.6px;">
        <li>Silversmithing</li>
        <li>Jewellery design and rendering</li>
        <li>Stone setting</li>
        <li>Gemmology</li>
        <li>Enamelling</li>
        <li>Computer aided design</li>
      </ul>
    </div>

    <div class="photo photo-rings" style="left:99px; top:872px; width:400px; height:142px;" role="img" aria-label="Row of gold and silver rings set with coloured gemstones"></div>
    <div class="photo photo-group" style="left:99px; top:1018px; width:400px; height:166px;" role="img" aria-label="Group of smiling students in aprons in the workshop"></div>

    <div class="abs band" style="left:99px; top:1184px; width:400px; height:16px;" role="img" aria-label="Teal woven lattice pattern band"></div>
  </section>

  <section class="poster-square">
    <div class="brand-mark" style="left:630px; top:580px; width:96px; height:96px;"></div>
    <div class="brand-name" style="left:528px; top:689px; width:300px; font-size:31px; letter-spacing:1px;">MIRA HOLLIS</div>
    <div class="brand-name" style="left:528px; top:725px; width:300px; font-size:17px; letter-spacing:3px;">jewellery</div>

    <h1 class="headline wrap" style="left:800px; top:588px; width:397px; font-size:31px; line-height:38px;">So you want to be a jewellery designer?</h1>
    <div class="abs" style="left:1098px; top:626px; width:80px; height:80px; border-radius:50%; background:var(--teal);" role="img" aria-label="Teal sunburst badge with wedding rings"></div>

    <div class="photo photo-tools" style="left:948px; top:680px; width:148px; height:136px;" role="img" aria-label="Jeweller's hammer, dividers and tweezers"></div>

    <h2 class="headline" style="left:546px; top:772px; width:392px; font-size:21.3px;">Part time and full-time classes available in:</h2>
    <ul class="course-list" style="left:546px; top:798px; width:392px; font-size:17.5px; line-height:21px; color:var(--text-dark);">
      <li>Silversmithing</li>
      <li>Jewellery design and rendering</li>
      <li>Stone setting</li>
      <li>Gemmology</li>
      <li>Enamelling</li>
      <li>Computer aided design</li>
    </ul>

    <div class="photo photo-class" style="left:546px; top:935px; width:396px; height:265px;" role="img" aria-label="Instructor guiding a student sawing metal at the bench"></div>
    <div class="photo photo-setting" style="left:945px; top:828px; width:255px; height:372px;" role="img" aria-label="Student in an apron setting stones while a teacher watches"></div>
  </section>

</div>
</body>
</html>
```